Cover Page for Financial Statements

We need a cover page designed for our Financial Statements. It will need to include our business logo and the Chartered accountant logo.
We have included our current title page ( image titled full.png ) to show all the information that is needed to be included such as the title 'Financial Statements' and 'The year ended March 2023'. We would like to see designs that reflect our logo but also adds some interest with objects / deisngs that fill up more of the page.

Industry/Entity Type

Accounting

Font styles to use
Serif
Sans Serif

Colors

Designer to choose only greyscale colors for use in the design.

Requirements
Must have
• - A4 document size, our logo, Chartered Accountant Logo
Should not have
• Bright Colors

```html
<!DOCTYPE html>
<html lang="en">
<head>
<meta charset="utf-8">
<title>Financial Statements Cover – Northvale Accounting &amp; Advisory Limited</title>
<link rel="stylesheet" href="https://fonts.googleapis.com/css2?family=Montserrat:wght@500;600;700;800&display=swap">
<style>
  :root {
    --backdrop: #c9c9c9;
    --charcoal: #2e2e31;
    --charcoal-deep: #242427;
    --title-grey: #58585c;
    --rule-dark: #111113;
    --panel-white: #f4f4f4;
    --ink: #1d1d1f;
    --white: #ffffff;
    --photo-light: #e6e6e6;
    --photo-mid: #a9a9ab;
    --photo-dark: #5c5c60;
  }
  * { box-sizing: border-box; margin: 0; padding: 0; }
  html, body {
    width: 1200px; height: 904px; overflow: hidden;
    background: var(--backdrop);
    font-family: "Montserrat", Arial, sans-serif;
  }
  .stage {
    position: relative; width: 1200px; height: 904px;
    display: flex; align-items: center; justify-content: center;
  }
  .cover {
    position: relative; width: 608px; height: 860px;
    background: var(--charcoal);
    overflow: hidden;
    box-shadow: 0 6px 18px rgba(0,0,0,0.18);
  }
  .cover-photo {
    position: absolute; left: 0; top: 0; width: 100%; height: 470px;
    background:
      radial-gradient(circle at 62% 48%, rgba(255,255,255,0.85) 0, rgba(255,255,255,0) 38%),
      linear-gradient(135deg, var(--photo-dark) 0%, var(--photo-mid) 40%, var(--photo-light) 100%);
  }
  .cover-base-band {
    position: absolute; left: 0; top: 470px; width: 100%; height: 390px;
    background: linear-gradient(180deg, var(--charcoal) 0%, var(--charcoal-deep) 100%);
  }
  .brand-panel {
    position: absolute; left: 48px; top: 300px; width: 350px; height: 128px;
    background: var(--panel-white);
    border-bottom: 3px solid var(--rule-dark);
    padding: 18px 22px 14px;
    display: flex; flex-direction: column; justify-content: space-between;
  }
  .brand-logos {
    display: flex; justify-content: space-between; align-items: center; gap: 12px;
  }
  .brand-mark {
    display: flex; align-items: center; gap: 7px;
    font-weight: 600; color: var(--ink);
  }
  .brand-mark__square {
    flex: 0 0 12px; width: 12px; height: 12px; background: var(--ink);
  }
  .brand-mark--institute { font-size: 7px; letter-spacing: 0.12em; text-transform: uppercase; max-width: 130px; line-height: 1.3; }
  .brand-mark--firm { font-size: 17px; letter-spacing: 0.14em; }
  .company-name {
    font-weight: 700; font-size: 17px; line-height: 1.2; color: var(--ink); text-align: center;
  }
  .title-block {
    position: absolute; left: 48px; top: 431px; width: 350px; height: 232px;
    background: var(--title-grey);
    padding: 34px 28px;
    color: var(--white);
  }
  .title-block__main {
    font-weight: 800; font-size: 50px; line-height: 0.98; letter-spacing: 0.01em;
  }
  .title-block__main span { display: block; }
  .title-block__main .sub-line { font-size: 44px; }
  .title-block__period {
    margin-top: 10px; font-weight: 600; font-size: 15px;
  }
</style>
</head>
<body>
  <main class="stage">
    <section class="cover">
      <div class="cover-photo" role="img" aria-label="Photograph of a business team joining fists together, overlaid with glowing digital circles"></div>
      <div class="cover-base-band"></div>

      <div class="brand-panel">
        <div class="brand-logos">
          <div class="brand-mark brand-mark--institute">
            <span class="brand-mark__square"></span>
            <span>Ledger Institute of Accountants</span>
          </div>
          <div class="brand-mark brand-mark--firm">
            <span class="brand-mark__square"></span>
            <span>NORTHVALE</span>
          </div>
        </div>
        <h2 class="company-name">Northvale Accounting<br>&amp; Advisory Limited</h2>
      </div>

      <div class="title-block">
        <h1 class="title-block__main">
          <span>Financial</span>
          <span class="sub-line">Statements</span>
        </h1>
        <p class="title-block__period">For the Year Ended 31 March, 2023</p>
      </div>
    </section>
  </main>
</body>
</html>
```